Clearwater Renewal Pathway Institute Second Chance Recovery Services

Logo needs to incorporate that we are here to help support positive healthy lifestyle change and help with restoration of drivers license after getting caught driving under the influence of alcohol or other drugs. While enrolled in our 3-,6-, or 9-mo program we help clients explore their relationship with alcohol or other drugs and and seek help and support so that can overcome barriers that support a healthy life style supporting client decisions to change risky behavior like driving under the influence of alcohol or drugs.

Target Market(s)

DWI / DUI Clients

Contact Information for Business Card

Logo that signifies supportive services for positive change

Requirements
Must have
• Its more of a Alcohol and drug program / Interventions for self assessment / evaluation of relationship with alcohol or drug and or risky behavior s
Should not have
• Cars on indication of cars sales

```html
<!DOCTYPE html>
<html lang="en">
<head>
<meta charset="utf-8">
<title>Clearwater Renewal Pathway Institute – Business Card</title>
<link rel="stylesheet" href="https://fonts.googleapis.com/css2?family=Jost:wght@400;500;700&display=swap">
<style>
  :root {
    --brand-red: #ff0000;
    --brand-black: #0a0a0a;
    --card-white: #ffffff;
    --ink: #111111;
    --faint-red: rgba(255, 0, 0, 0.09);
    --stage-top: #fbfbfb;
    --stage-bottom: #e6e6e6;
  }
  * { box-sizing: border-box; margin: 0; padding: 0; }
  html, body {
    width: 1200px;
    height: 1028px;
    overflow: hidden;
  }
  body {
    position: relative;
    background: linear-gradient(180deg, var(--stage-top) 0%, var(--stage-bottom) 100%);
    font-family: "Jost", "Futura", sans-serif;
    color: var(--ink);
  }
  .card {
    position: absolute;
    left: 259px;
    width: 682px;
    height: 389px;
    background: var(--card-white);
    box-shadow: 0 4px 14px rgba(0,0,0,0.35);
    overflow: hidden;
  }
  .card--front { top: 78px; }
  .card--back  { top: 532px; }
  .card__bands {
    position: absolute;
    inset: 0;
    width: 100%;
    height: 100%;
  }

  /* Front */
  .brand__dot {
    position: absolute;
    left: 175px;
    top: 102px;
    width: 90px;
    height: 90px;
    border-radius: 50%;
    background: var(--brand-red);
  }
  .brand__name {
    position: absolute;
    left: 60px;
    top: 232px;
    width: 320px;
    text-align: center;
    font-weight: 700;
    font-size: 23px;
    line-height: 1.2;
    letter-spacing: 0.3px;
    text-transform: uppercase;
    color: var(--ink);
  }

  /* Back: faint brand mark */
  .backmark__dot {
    position: absolute;
    left: 330px;
    top: 100px;
    width: 120px;
    height: 120px;
    border-radius: 50%;
    background: var(--faint-red);
  }
  .backmark__name {
    position: absolute;
    left: 465px;
    top: 104px;
    font-weight: 700;
    font-size: 30px;
    line-height: 1.2;
    text-transform: uppercase;
    color: var(--faint-red);
    white-space: nowrap;
  }

  .holder__bar {
    position: absolute;
    left: 335px;
    top: 42px;
    width: 5px;
    height: 53px;
    border-radius: 3px;
    background: var(--brand-black);
  }
  .holder__name {
    position: absolute;
    left: 366px;
    top: 42px;
    font-weight: 700;
    font-size: 25px;
    line-height: 1;
  }
  .holder__role {
    position: absolute;
    left: 366px;
    top: 70px;
    font-weight: 500;
    font-size: 15px;
  }
  .contact {
    position: absolute;
    left: 335px;
    top: 0;
    list-style: none;
    font-size: 17px;
    line-height: 23px;
  }
  .contact__item {
    position: absolute;
    left: 0;
    display: flex;
    align-items: center;
    white-space: nowrap;
  }
  .contact__icon {
    width: 22px;
    height: 22px;
    margin-right: 8px;
    fill: var(--brand-black);
    flex: none;
  }
</style>
</head>
<body>

<section class="card card--front" aria-label="Business card front">
  <svg class="card__bands" viewBox="0 0 568 324" preserveAspectRatio="none" aria-hidden="true">
    <defs>
      <filter id="band-shadow-front" x="-20%" y="-20%" width="140%" height="140%">
        <feDropShadow dx="4" dy="0" stdDeviation="4" flood-color="#000" flood-opacity="0.45"/>
      </filter>
    </defs>
    <rect width="568" height="324" fill="var(--brand-red)"/>
    <polygon points="0,0 384,0 474,160 384,324 0,324" fill="var(--brand-red)" filter="url(#band-shadow-front)"/>
    <polygon points="0,0 344,0 434,160 344,324 0,324" fill="var(--brand-black)" filter="url(#band-shadow-front)"/>
    <polygon points="0,0 304,0 392,160 304,324 0,324" fill="var(--card-white)" filter="url(#band-shadow-front)"/>
  </svg>
  <span class="brand__dot"></span>
  <p class="brand__name">Clearwater Renewal<br>Pathway Institute</p>
</section>

<section class="card card--back" aria-label="Business card back">
  <svg class="card__bands" viewBox="0 0 568 324" preserveAspectRatio="none" aria-hidden="true">
    <defs>
      <filter id="band-shadow-back" x="-20%" y="-20%" width="140%" height="140%">
        <feDropShadow dx="-4" dy="0" stdDeviation="4" flood-color="#000" flood-opacity="0.45"/>
      </filter>
    </defs>
    <rect width="568" height="324" fill="var(--brand-red)"/>
    <polygon points="184,0 568,0 568,324 184,324 94,163" fill="var(--brand-red)" filter="url(#band-shadow-back)"/>
    <polygon points="224,0 568,0 568,324 224,324 134,163" fill="var(--brand-black)" filter="url(#band-shadow-back)"/>
    <polygon points="264,0 568,0 568,324 264,324 176,163" fill="var(--card-white)" filter="url(#band-shadow-back)"/>
  </svg>

  <span class="backmark__dot" aria-hidden="true"></span>
  <span class="backmark__name" aria-hidden="true">Clearwater<br>Renewal<br>Pathway</span>

  <span class="holder__bar"></span>
  <h1 class="holder__name">YOUR NAME</h1>
  <p class="holder__role">Managing Director</p>

  <ul class="contact">
    <li class="contact__item" style="top:170px">
      <svg class="contact__icon" viewBox="0 0 24 24" aria-label="Phone"><path d="M6.6 10.8a15.1 15.1 0 0 0 6.6 6.6l2.2-2.2a1 1 0 0 1 1-.25 11.4 11.4 0 0 0 3.6.57 1 1 0 0 1 1 1V20a1 1 0 0 1-1 1A17 17 0 0 1 3 4a1 1 0 0 1 1-1h3.5a1 1 0 0 1 1 1c0 1.25.2 2.45.57 3.57a1 1 0 0 1-.25 1z"/></svg>
      <span>+1 555 201 XXX<br>+1 555 202 XXX</span>
    </li>
    <li class="contact__item" style="top:223px">
      <svg class="contact__icon" viewBox="0 0 24 24" aria-label="Address"><path d="M12 2a7 7 0 0 0-7 7c0 5.2 7 13 7 13s7-7.8 7-13a7 7 0 0 0-7-7zm0 9.5A2.5 2.5 0 1 1 12 6.5a2.5 2.5 0 0 1 0 5z"/></svg>
      <span>48 Willow Lane<br>Riverbend, CA 960XX</span>
    </li>
    <li class="contact__item" style="top:278px">
      <svg class="contact__icon" viewBox="0 0 24 24" aria-label="Email"><path d="M3 5h18a1 1 0 0 1 1 1v12a1 1 0 0 1-1 1H3a1 1 0 0 1-1-1V6a1 1 0 0 1 1-1zm0 2.2V17h18V7.2l-9 6-9-6zM4.3 7 12 12l7.7-5z"/></svg>
      <span>renewalpathway1223@xxmail.com</span>
    </li>
    <li class="contact__item" style="top:306px">
      <svg class="contact__icon" viewBox="0 0 24 24" aria-label="Website"><path d="M6 3v16l4.2-4 2.8 6.5 2.6-1.1-2.8-6.4H18z"/></svg>
      <span>www.renewalpathway.net<br>info@renewalpathway.net</span>
    </li>
  </ul>
</section>

</body>
</html>
```